Home loan promotion flyer (DL or Postcard)

We need a flyer that promotes our home loan broking service. In summary, we are an Australian financial planning business that helps Gen X and Y make better financial planning decisions.

We would like the design to have a similar look and feel to the following:
http://www.leaflet-vault.com.au/qmpr/bright_path_steady_living/

Text that I would like included is:

(HEADING) Awesome Debt Management: Someone else's money used to Your advantage.

(Paragraph) Debt is not necessarily a dirty work. Smart Australian investors often use debt strategies to minimise tax burdens, pay off their home loan sooner and to build their wealth quicker.

(Promotion) Bring this along to your COMPLIMENTARY finance health check and we will give you a $25 Durban Vale voucher to celebrate your first step towards a better financial future. (Please include the image of the voucher near this text).

Finally, you must include our number (1300 614 972) and website (www.qmpr.com.au)

Apart from being consistent with the e-brochure above (please ensure you view the link), we would like the design to be bold and stand out from the crowd.

I have attached a previous home loan promotion design that I like but I feel that there are too many words and not enough space. Please use the good elements but avoid the rest.

Finally, I've also attached a DL "goldfish" design that I really like because I think the design is memorable and stands-out.
Updates

Reason: Hi there designers Thanks for your designs so far. They look great. I have extended the brief to give everyone the opportunity to reassess their design to make sure that it is consistent with the design brief. If anything is unclear please don't hesitate to make contact. Thanks TR

Target Market(s)

Australian first home buyers and property investors.

Industry/Entity Type

Financial

Requirements
Must have
• The design MUST be consistent with the existing marketing material referred to in this link.

```html
<!DOCTYPE html>
<html lang="en">
<head>
<meta charset="utf-8">
<title>Awesome Debt Management Postcard</title>
<link rel="stylesheet" href="https://fonts.googleapis.com/css2?family=Montserrat:wght@500;700;800&family=Questrial&display=swap">
<style>
  :root {
    --page: #e9e9e7;
    --card-dark: #262626;
    --panel-dark: #2d2d2d;
    --green: #5aa745;
    --green-bright: #6cc04a;
    --white: #ffffff;
    --text-soft: #e4e4e4;
    --rule: #6a6a6a;
    --photo-light: #a9adaf;
    --photo-dark: #55595c;
  }
  * { box-sizing: border-box; margin: 0; padding: 0; }
  html, body { width: 1200px; height: 1200px; overflow: hidden; }
  body {
    background: var(--page);
    font-family: "Questrial", "Helvetica Neue", Arial, sans-serif;
    position: relative;
  }
  .card {
    position: absolute;
    left: 100px;
    width: 1000px;
    height: 480px;
    overflow: hidden;
    box-shadow: 0 10px 26px rgba(0,0,0,0.22);
  }
  /* Front */
  .card--front { top: 90px; background: var(--panel-dark); }
  .front__photo {
    position: absolute; inset: 0;
    background: radial-gradient(ellipse at 62% 45%, var(--photo-dark) 0%, #7d8184 40%, var(--photo-light) 100%);
  }
  .front__curve { position: absolute; inset: 0; }
  .brand {
    position: absolute;
    display: flex; align-items: center; gap: 8px;
    color: var(--white);
    font-family: "Questrial", Arial, sans-serif;
    font-size: 17px;
    line-height: 1.1;
  }
  .brand__mark { width: 22px; height: 22px; background: var(--green-bright); flex: none; }
  .card--front .brand { right: 28px; top: 34px; }

  /* Back */
  .card--back { top: 630px; background: var(--card-dark); color: var(--white); }
  .back__band { position: absolute; top: 0; left: 0; right: 0; height: 14px; background: var(--green); }
  .headline { position: absolute; left: 30px; top: 52px; }
  .headline__lead {
    font-family: "Montserrat", Arial, sans-serif;
    font-weight: 800; font-size: 32px; color: var(--green-bright);
    letter-spacing: 0.2px;
  }
  .headline__lead span { color: var(--white); font-weight: 500; }
  .headline__sub {
    font-family: "Montserrat", Arial, sans-serif;
    font-weight: 500; font-size: 26px; color: var(--white); margin-top: 2px;
  }
  .headline__sub strong { color: var(--green-bright); font-weight: 700; }
  .stamp {
    position: absolute; right: 40px; top: 30px;
    width: 104px; height: 74px;
    background: var(--white);
    border: 2px dashed var(--green);
    display: flex; align-items: center; justify-content: center; text-align: center;
    color: #1d1d1d; font-size: 23px; line-height: 1;
  }
  .card--back .brand { right: 40px; top: 122px; font-size: 15px; }
  .intro {
    position: absolute; left: 30px; top: 148px; width: 610px;
    font-size: 16px; line-height: 1.45; color: var(--text-soft);
    text-indent: 12px;
  }
  .rule { position: absolute; left: 30px; top: 242px; width: 820px; height: 1px; background: var(--rule); }
  .offer { position: absolute; left: 30px; top: 262px; width: 330px; font-size: 16px; line-height: 1.35; color: var(--text-soft); }
  .offer strong { font-family: "Montserrat", Arial, sans-serif; font-weight: 700; color: var(--white); }
  .voucher {
    margin: 10px 0 14px;
    width: 300px; height: 38px;
    background: var(--green);
    border: 2px dashed #c9e6bd;
    display: flex; align-items: center; justify-content: center;
    color: #121212; font-family: "Montserrat", Arial, sans-serif; font-weight: 600; font-size: 16px;
  }
  .voucher b { font-weight: 800; }
  .contact { position: absolute; left: 30px; top: 418px; font-size: 15px; line-height: 1.3; color: var(--text-soft); }
  .mailing {
    position: absolute; left: 470px; top: 258px;
    width: 400px; height: 172px;
    background: var(--white);
    border: 3px dashed var(--green);
    display: flex; align-items: center; justify-content: center;
    color: #1d1d1d; font-size: 17px;
  }
</style>
</head>
<body>

<section class="card card--front">
  <div class="front__photo" role="img" aria-label="Photo of a businessman in a suit drawing financial analysis sketches and charts on a glass board"></div>
  <svg class="front__curve" viewBox="0 0 1000 480" aria-hidden="true">
    <path d="M540 0 C 720 60, 860 230, 1000 470 L1000 0 Z" fill="var(--panel-dark)"/>
    <path d="M540 0 C 720 60, 860 230, 1000 470" fill="none" stroke="var(--green-bright)" stroke-width="4"/>
  </svg>
  <div class="brand"><span class="brand__mark"></span><span>Quill Meadow<br>Planning</span></div>
</section>

<section class="card card--back">
  <div class="back__band"></div>
  <header class="headline">
    <h1 class="headline__lead">AWESOME DEBT MANAGEMENT<span>:</span></h1>
    <p class="headline__sub">Someone else's money used to <strong>Your advantage.</strong></p>
  </header>
  <div class="stamp">POST<br>CARD</div>
  <div class="brand"><span class="brand__mark"></span><span>Quill Meadow<br>Planning</span></div>
  <p class="intro">Debt is not necessarily a dirty work. Smart Australian investors often use debt strategies to minimise tax burdens, pay off their home loan sooner and to build their wealth quicker.</p>
  <div class="rule"></div>
  <div class="offer">
    <p>Bring this along to your <strong>COMPLIMENTARY</strong> finance health check and we will give you a</p>
    <div class="voucher">$25&nbsp;<b>Durban Vale</b>&nbsp;voucher</div>
    <p>to celebrate your first step towards a <strong>better financial future.</strong></p>
  </div>
  <p class="contact">1300 614 972 give us a call<br>www.qmpr.com.au</p>
  <div class="mailing">mailing address</div>
</section>

</body>
</html>
```